TM Holdings-Homes for Tomorrow's World

TM Holdings is a Residential Real Estate company which specializes in buying and selling homes. We pride ourselves on service, expertise, and building relationships. I would like to do a Billboard Ad for a The Size is 14 feet (Height) x 48 feet (width) displaying our current motto for "Real Estate of the Future" We have launched new programs and working with leaders in our industy Pavrit and other tech companies and changing the way Real Estate is done in Las Vegas, NV. Its exciting and NEW so we want to get the word out. Color Scheme Red, White, Grey and maybe black. Logo is uploaded and so is a picture head shot. I would like to see options with my headshot and with out.

```html
<!DOCTYPE html>
<html lang="en">
<head>
<meta charset="utf-8">
<title>TM Holdings – Billboard</title>
<link rel="stylesheet" href="https://fonts.googleapis.com/css2?family=Arvo:wght@700&family=Libre+Baskerville:wght@400;700&display=swap">
<style>
  :root {
    --brand-red: #c00000;
    --ink: #2e2e33;
    --swoosh-grey: #3f4349;
    --band-grey: #efeff1;
    --paper: #ffffff;
    --stage: #e4e7eb;
    --sky-top: #7fb4e6;
    --sky-low: #dce9f5;
    --house-tone: #b9ab9c;
    --people-tone: #e6c3a4;
  }
  * { margin: 0; padding: 0; box-sizing: border-box; }
  html, body { width: 1200px; height: 900px; overflow: hidden; }
  body { background: var(--stage); position: relative; }

  .billboard {
    position: absolute; left: 0; top: 275px;
    width: 1200px; height: 350px;
    background: var(--paper);
    overflow: hidden;
  }
  .billboard__shapes { position: absolute; inset: 0; }

  .headline {
    position: absolute; left: 727px; top: 8px;
    color: var(--paper);
    font-family: "Arvo", Georgia, serif; font-weight: 700;
    line-height: 1;
  }
  .headline__main { display: block; font-size: 56px; letter-spacing: 1px; }
  .headline__sub { display: flex; align-items: flex-end; margin-top: -4px; }
  .headline__rule {
    width: 144px; height: 8px; margin: 0 6px 13px 0;
    border-top: 2px solid var(--paper); border-bottom: 2px solid var(--paper);
  }
  .headline__small { font-size: 25px; margin: 0 12px 11px 0; }
  .headline__big { font-size: 56px; letter-spacing: 1px; }

  .brand-name {
    position: absolute; left: 736px; top: 196px;
    font-family: "Libre Baskerville", Georgia, serif; font-weight: 400;
    font-size: 46px; color: var(--brand-red);
    letter-spacing: 2px; line-height: 1.2;
  }

  .tagline {
    position: absolute; left: 47px; top: 262px;
    padding-left: 14px; border-left: 3px solid var(--ink);
    font-family: "Libre Baskerville", Georgia, serif; font-weight: 700;
    font-size: 22.5px; line-height: 33px; color: var(--ink);
    text-transform: uppercase; letter-spacing: 0.3px;
  }
  .tagline em { font-style: normal; color: var(--brand-red); }

  .phone {
    position: absolute; left: 766px; top: 296px;
    display: flex; align-items: center; gap: 12px;
    font-family: "Libre Baskerville", Georgia, serif; font-weight: 700;
    font-size: 39px; line-height: 1; color: var(--ink); letter-spacing: 1px;
  }
  .phone__icon { width: 38px; height: 38px; flex: none; }
</style>
</head>
<body>
  <section class="billboard" aria-label="TM Holdings billboard">
    <svg class="billboard__shapes" viewBox="0 0 1200 350" width="1200" height="350">
      <defs>
        <linearGradient id="hero-sky" x1="0" y1="0" x2="0" y2="1">
          <stop offset="0" stop-color="var(--sky-top)"/>
          <stop offset="1" stop-color="var(--sky-low)"/>
        </linearGradient>
        <linearGradient id="hero-tones" x1="0" y1="0" x2="1" y2="0">
          <stop offset="0" stop-color="var(--people-tone)" stop-opacity="0.9"/>
          <stop offset="0.26" stop-color="var(--people-tone)" stop-opacity="0.5"/>
          <stop offset="0.4" stop-color="var(--house-tone)" stop-opacity="0.0"/>
          <stop offset="0.6" stop-color="var(--house-tone)" stop-opacity="0.75"/>
          <stop offset="0.95" stop-color="var(--house-tone)" stop-opacity="0.2"/>
        </linearGradient>
      </defs>

      <g class="hero-photo" role="img" aria-label="Photo of a smiling couple in front of a brick family home under a blue sky">
        <rect x="0" y="0" width="720" height="290" fill="url(#hero-sky)"/>
        <rect x="0" y="60" width="720" height="230" fill="url(#hero-tones)"/>
      </g>

      <path class="panel-white" d="M608 211 Q900 120 1200 164 V350 H608 Z" fill="var(--paper)"/>

      <path class="panel-red" d="M683 0 H1200 V164 Q900 120 608 211 C690 160 712 70 683 0 Z"
            fill="var(--brand-red)" stroke="var(--paper)" stroke-width="12" paint-order="stroke"/>
      <path class="swoosh-upper" d="M608 211 Q900 120 1200 164 V192 Q900 142 608 211 Z" fill="var(--swoosh-grey)"/>

      <path class="band-lower" d="M0 253 C150 215 400 205 762 285 C950 300 1100 280 1200 257 V350 H0 Z"
            fill="var(--band-grey)"/>
      <path class="swoosh-lower" d="M0 253 C150 215 400 205 762 285 C950 300 1100 280 1200 257"
            fill="none" stroke="var(--swoosh-grey)" stroke-width="5"/>
    </svg>

    <h1 class="headline">
      <span class="headline__main">Real Estate</span>
      <span class="headline__sub">
        <span class="headline__rule"></span>
        <span class="headline__small">of the</span>
        <span class="headline__big">Future</span>
      </span>
    </h1>

    <div class="brand-name">TM HOLDINGS</div>

    <p class="tagline">
      We pride ourselves on <em>service</em>,<br>
      <em>expertise</em>, and <em>building relationships</em>.
    </p>

    <div class="phone">
      <svg class="phone__icon" viewBox="0 0 36 36" aria-hidden="true">
        <circle cx="18" cy="18" r="16" fill="none" stroke="var(--ink)" stroke-width="2"/>
        <path d="M12 10 l4 -1 2 5 -2.5 2 c1 2.5 3 4.5 5.5 5.5 l2 -2.5 5 2 -1 4 c-8 1 -16 -7 -15 -15 z" fill="var(--brand-red)"/>
      </svg>
      <span class="phone__number">0145-678-902</span>
    </div>
  </section>
</body>
</html>
```